HTML newsletter template for construction company

Hello. I need a company newsletter template made. Our website is: www.harrowmintwork.com

Can you please spend some time on our website and design a similarly themed newsletter template for us? We use infusionsoft, so it'd be great if someone has experience with infusionsoft's newsletter requirements.

Target Market(s)

All sized subcontracting companies. We are a national company but are headquartered in Phoenix, Az.

Industry/Entity Type

Construction Company

Font styles to use
Sans Serif

Requirements
Must have
• html
Nice to have
• We need a few different "sections" for content. We're planning on having an interview, a construction project spotlight, some type of article, tips of some-sort and provide a few upcoming events that we are participating in.

```html
<!DOCTYPE html>
<html lang="en">
<head>
<meta charset="utf-8">
<title>Harrowmint Work Newsletter – First Edition</title>
<link href="https://fonts.googleapis.com/css2?family=Nunito+Sans:wght@300;400;700;800&family=Roboto:wght@400;700&display=swap" rel="stylesheet">
<style>
  :root {
    --stage: #ffc96b;
    --paper: #ffffff;
    --ink: #1f2124;
    --charcoal: #25282b;
    --blue: #4285c7;
    --orange: #df5a2a;
    --gold: #f2b450;
    --muted: #c9ccd0;
  }
  * { box-sizing: border-box; margin: 0; padding: 0; }
  html, body { width: 900px; height: 1200px; overflow: hidden; }
  body {
    background: var(--stage);
    font-family: "Nunito Sans", Arial, sans-serif;
    color: var(--ink);
    position: relative;
  }
  .newsletter {
    position: absolute; left: 203px; top: 20px;
    width: 494px; height: 1160px;
    background: var(--paper);
    box-shadow: 4px 5px 8px rgba(0,0,0,.25);
    overflow: hidden;
  }
  .abs { position: absolute; }

  /* Header */
  .brand-mark { left: 54px; top: 30px; width: 64px; height: 64px; border-radius: 50%; background: var(--blue); }
  .brand-name { left: 30px; top: 98px; font-size: 19px; font-weight: 400; color: var(--ink); letter-spacing: -.3px; }
  .masthead { right: 30px; top: 42px; text-align: right; }
  .masthead-title { font-size: 38px; line-height: 40px; letter-spacing: .5px; }
  .masthead-title .news { color: var(--blue); font-weight: 800; }
  .masthead-title .letter { color: var(--ink); font-weight: 400; }
  .masthead-sub { font-size: 16px; color: var(--blue); letter-spacing: .4px; margin-top: -1px; }

  /* Bars */
  .edition-bar {
    left: 0; top: 134px; width: 494px; height: 16px;
    background: var(--orange); color: #fff;
    font-size: 12px; font-weight: 700;
    display: flex; justify-content: space-between; align-items: center;
    padding: 0 30px;
  }
  .section-bar {
    left: 0; width: 494px; height: 28px;
    background: var(--charcoal); color: #fff;
    font-size: 17px; font-weight: 400; letter-spacing: .3px;
    display: flex; align-items: center; padding-left: 30px;
  }
  .section-bar .chevron { font-size: 13px; margin-left: 14px; font-weight: 700; }
  .section-bar.orange { background: var(--orange); }

  /* Stories */
  .stories { left: 0; top: 185px; width: 494px; height: 217px; }
  .story-edge { position: absolute; top: 0; height: 217px; background: var(--blue); }
  .story-card {
    position: absolute; top: 0; width: 142px; height: 217px;
    background: var(--blue); color: #fff; text-align: center;
  }
  .story-kind { margin-top: 9px; font-size: 18px; font-weight: 800; line-height: 20px; }
  .story-of { font-size: 12px; font-weight: 300; line-height: 14px; opacity: .95; }
  .story-photo {
    width: 110px; height: 114px; margin: 7px auto 0;
    border: 3px solid #fff;
  }
  .story-name { margin-top: 7px; font-size: 12px; font-weight: 800; line-height: 13px; }
  .story-role { font-size: 10px; font-weight: 300; line-height: 12px; }
  .story-link { font-size: 10px; color: var(--gold); line-height: 14px; margin-top: 2px; }

  /* Portal banner */
  .portal {
    left: 0; top: 407px; width: 494px; height: 161px;
    background: radial-gradient(ellipse at 30% 60%, #4a4d52 0%, #2f3236 55%, #222427 100%);
    color: #fff; text-align: center;
  }
  .portal-title { margin-top: 43px; font-size: 26px; font-weight: 800; letter-spacing: .5px; line-height: 30px; }
  .portal-sub { font-size: 16px; font-weight: 300; letter-spacing: .4px; }

  /* Interview */
  .interview-copy {
    position: absolute; left: 45px; width: 405px;
    font-size: 11.5px; line-height: 13.8px; letter-spacing: -.2px;
    text-align: justify; hyphens: auto;
  }
  .interview-copy.lead { width: 282px; }
  .interview-name { font-weight: 700; }
  .interview-photo { left: 344px; top: 622px; width: 106px; height: 109px; background: linear-gradient(160deg, #7f9aa8, #3a4656 60%, #1f2a38); }

  /* Testimonials */
  .voices { left: 0; top: 963px; width: 494px; height: 154px; background: var(--charcoal); color: #fff; font-family: "Roboto", Arial, sans-serif; }
  .voices-title { position: absolute; top: 16px; width: 100%; text-align: center; font-size: 16px; font-weight: 700; }
  .voices-rule { position: absolute; left: 192px; top: 36px; }
  .quote { position: absolute; top: 70px; }
  .quote-text { font-size: 5.6px; line-height: 7.3px; }
  .quote-by { font-size: 5.5px; color: var(--muted); margin-top: 6px; }
  .quote-mark { position: absolute; top: 72px; }
  .read-more {
    position: absolute; left: 222px; top: 123px; width: 51px; height: 14px;
    border: 1px solid #fff; border-radius: 2px;
    font-size: 5.5px; text-align: center; line-height: 12px;
  }
</style>
</head>
<body>
<main class="newsletter">
  <header>
    <div class="abs brand-mark"></div>
    <div class="abs brand-name">Harrowmint Work</div>
    <div class="abs masthead">
      <div class="masthead-title"><span class="news">NEWS</span><span class="letter">LETTER</span></div>
      <div class="masthead-sub">MONTHLY EDITIONS</div>
    </div>
  </header>

  <div class="abs edition-bar"><span>FIRST EDITION</span><span>21st August 2016</span></div>
  <div class="abs section-bar" style="top:153px;">THIS MONTH STORIES <span class="chevron">❯</span></div>

  <section class="abs stories">
    <div class="story-edge" style="left:0;width:23px;"></div>
    <article class="story-card" style="left:29px;">
      <div class="story-kind">INTERVIEW</div>
      <div class="story-of">OF THE MONTH</div>
      <div class="story-photo" role="img" aria-label="Portrait photo of the company's chief executive" style="background:linear-gradient(160deg,#8ea3a5,#3d4a58 60%,#1f2a38);"></div>
      <div class="story-name">Marcus Ellery</div>
      <div class="story-role">Chief Executive Officer</div>
      <div class="story-link">More Interviews</div>
    </article>
    <article class="story-card" style="left:177px;">
      <div class="story-kind">PROJECT</div>
      <div class="story-of">OF THE MONTH</div>
      <div class="story-photo" role="img" aria-label="Photo of a construction worker in a hard hat on site" style="background:linear-gradient(170deg,#c9a77a,#5a6f9a 55%,#24305a);"></div>
      <div class="story-name">Revolving Lines</div>
      <div class="story-role">A Master Credit Line</div>
      <div class="story-link">More Projects</div>
    </article>
    <article class="story-card" style="left:325px;">
      <div class="story-kind">ARTICLE</div>
      <div class="story-of">OF THE MONTH</div>
      <div class="story-photo" role="img" aria-label="Photo of an engineer in a hard hat overlooking a building site" style="background:linear-gradient(180deg,#eef1f3,#d9d3c8 55%,#8f8a80);"></div>
      <div class="story-name">A Desire For Change</div>
      <div class="story-role">Marcus Ellery</div>
      <div class="story-link">More Articles</div>
    </article>
    <div class="story-edge" style="left:473px;width:21px;"></div>
  </section>

  <section class="abs portal" role="img" aria-label="Dimmed photo of hands working on a laptop, behind the portal tour heading">
    <div class="portal-title">TOUR OUR PORTAL</div>
    <div class="portal-sub">Explore the Dashboard &amp; Other Features</div>
  </section>

  <div class="abs section-bar" style="top:572px;">INTERVIEW OF THE MONTH <span class="chevron">❯</span></div>

  <section class="interview">
    <p class="interview-copy lead" style="top:622px;"><span class="interview-name">Marcus Ellery, Chief Executive Officer</span><br>Lorem ipsum dolor sit amet, consectetuer adipiscing elit, sed diam nonummy nibh euismod tincidunt ut laoreet dolore magna aliquam erat volutpat. Ut wisi enim ad minim veniam, quis nostrud exerci tation ullamcorper suscipit lobortis nisl ut aliquip ex ea commodo consequat. Duis autem vel eum Duis autem vel eum Duis autem vel eum Duis autem vel eum</p>
    <p class="interview-copy" style="top:747px;">Lorem ipsum dolor sit amet, consectetuer adipiscing elit, sed diam nonummy nibh euismod tincidunt ut laoreet dolore magna aliquam erat volutpat. Ut wisi enim ad minim veniam, quis nostrud exerci tation ullamcorper suscipit lobortis nisl ut aliquip ex ea commodo consequat. Duis autem vel eum</p>
    <p class="interview-copy" style="top:816px;">Lorem ipsum dolor sit amet, consectetuer adipiscing elit, sed diam nonummy nibh euismod tincidunt ut laoreet dolore magna aliquam erat volutpat. Ut wisi enim ad minim veniam, quis nostrud exerci tation ullamcorper suscipit lobortis nisl ut aliquip ex ea commodo consequat. Duis autem vel eum</p>
    <p class="interview-copy" style="top:885px;">Lorem ipsum dolor sit amet, consectetuer adipiscing elit, sed diam nonummy nibh euismod tincidunt ut laoreet dolore magna aliquam erat volutpat. Ut wisi enim ad minim veniam, quis nostrud exerci tation ullamcorper suscipit lobortis nisl ut aliquip ex ea commodo consequat. Duis autem vel eum</p>
  </section>
  <div class="abs interview-photo" role="img" aria-label="Portrait photo of the chief executive"></div>

  <section class="abs voices">
    <div class="voices-title">What Our Customers Are Saying</div>
    <svg class="voices-rule" width="110" height="12" viewBox="0 0 110 12">
      <line x1="0" y1="6" x2="48" y2="6" stroke="#6b6f74" stroke-width="1"/>
      <line x1="62" y1="6" x2="110" y2="6" stroke="#6b6f74" stroke-width="1"/>
      <circle cx="55" cy="6" r="4.5" fill="#4285c7" stroke="#fff" stroke-width="1"/>
    </svg>

    <svg class="quote-mark" style="left:42px;" width="40" height="34" viewBox="0 0 40 34">
      <path d="M2 2h15v10l-8 20H3l5-16H2z" fill="#fff" stroke="#4285c7" stroke-width="2"/>
      <path d="M22 2h15v10l-8 20h-6l5-16h-6z" fill="#fff" stroke="#4285c7" stroke-width="2"/>
    </svg>
    <div class="quote" style="left:89px;width:150px;">
      <div class="quote-text">"Working with Harrowmint Work is great. Everyone is easy to work with. Anytime I've ever needed help I've always gotten an immediate answer and everyone is so easy and helpful. It's like no one ever has a bad day over there!"</div>
      <div class="quote-by">- Dana, Controller</div>
    </div>

    <svg class="quote-mark" style="left:252px;" width="40" height="34" viewBox="0 0 40 34">
      <path d="M2 2h15v10l-8 20H3l5-16H2z" fill="#fff" stroke="#df5a2a" stroke-width="2"/>
      <path d="M22 2h15v10l-8 20h-6l5-16h-6z" fill="#fff" stroke="#df5a2a" stroke-width="2"/>
    </svg>
    <div class="quote" style="left:299px;width:160px;">
      <div class="quote-text">"On projects that are supply intensive we get a 2–5 % discount, which is huge in our industry. It's just unheard of, but when you pay so quickly, the suppliers are happy to provide it."</div>
      <div class="quote-by">- Priya, CFO</div>
    </div>

    <div class="read-more">Read More</div>
  </section>

  <div class="abs section-bar orange" style="top:1122px;height:27px;">PROJECT OF THE MONTH <span class="chevron" style="margin-left:30px;">❯</span></div>
</main>
</body>
</html>
```